Coastal Bright Sweep Business Card

We are a cleaning and waste management company with the slogan "Turning everyday waste into tomorrow's uses". We would like a re-design of our current business card. On the front we want to continue to use our logo as the focus point. On the back, we want the whole thing re-done to be less busy. We want the staff member’s name, the job title, mobile number, email and website. We do not want the address on the card. We still want the green, black and blue colours used, but a new font for the information on the back. Please do not change the logo design at all. We are also thinking about using icons to replace the text ‘mobile, email, website’. The “events + commercial” banner needs to be incorporated somewhere and needs to read “events + commercial + waste”. Another important point for consideration is that we are very concerned about being environmentally sustainable and will be printing on recycled paper. All designs should be made to compliment this in regards to boldness and colouring. Please find attached our logo, our colour chart and an image of our current business card.

```html
<!DOCTYPE html>
<html lang="en">
<head>
<meta charset="utf-8">
<title>Coastal Bright Sweep Business Card</title>
<link href="https://fonts.googleapis.com/css2?family=Open+Sans:wght@400;600;700&family=Roboto+Condensed:wght@400;700&display=swap" rel="stylesheet">
<style>
  :root {
    --backdrop: #e9e6e1;
    --card-white: #f4f4f4;
    --navy: #0d3a72;
    --panel-navy: #0f4074;
    --sky: #1ea5e0;
    --leaf: #7cc242;
    --ink-white: #ffffff;
  }
  * { margin: 0; padding: 0; box-sizing: border-box; }
  html, body {
    width: 1200px; height: 960px; overflow: hidden;
    background: var(--backdrop);
  }
  .stage { position: relative; width: 1200px; height: 960px; }

  .card {
    position: absolute;
    width: 600px; height: 343px;
    border-radius: 20px;
    overflow: hidden;
    box-shadow: 0 3px 6px rgba(0,0,0,0.25);
  }

  /* front */
  .card-front { left: 314px; top: 113px; background: var(--card-white); }
  .accent-tab {
    position: absolute; left: 0; top: 91px;
    width: 9px; height: 161px;
    background: var(--sky);
    border-radius: 0 4px 4px 0;
  }
  .brand-name {
    position: absolute; left: 44px; top: 110px; width: 200px;
    font-family: "Roboto Condensed", sans-serif;
    font-weight: 700; font-size: 38px; line-height: 40px;
    color: var(--navy);
    text-align: center;
  }
  .contact-panel {
    position: absolute; left: 267px; top: 91px;
    width: 333px; height: 160px;
    background: var(--panel-navy);
    border-radius: 8px 0 0 8px;
    color: var(--ink-white);
    padding: 17px 0 0 20px;
  }
  .staff-name {
    font-family: "Roboto Condensed", sans-serif;
    font-weight: 700; font-size: 21px; line-height: 26px;
    letter-spacing: 0.3px;
  }
  .staff-role {
    font-family: "Roboto Condensed", sans-serif;
    font-size: 15px; line-height: 20px; letter-spacing: 0.5px;
  }
  .contact-list { list-style: none; margin-top: 20px; }
  .contact-list li {
    display: flex; align-items: center; gap: 7px;
    font-family: "Open Sans", sans-serif;
    font-size: 13.5px; line-height: 19.5px;
  }
  .contact-list svg { width: 12px; height: 12px; flex: none; }

  /* back */
  .card-back { left: 311px; top: 472px; background: var(--navy); }
  .back-brand {
    position: absolute; left: 0; right: 0; top: 120px;
    text-align: center;
    font-family: "Roboto Condensed", sans-serif;
    font-weight: 700; font-size: 46px; line-height: 54px;
    color: var(--sky);
  }
  .slogan {
    position: absolute; right: 105px; top: 196px;
    font-family: "Open Sans", sans-serif;
    font-weight: 700; font-size: 13.5px;
    color: var(--ink-white);
    white-space: nowrap;
  }
  .service-line {
    position: absolute; left: 0; right: 0; top: 279px;
    text-align: center;
    font-family: "Open Sans", sans-serif;
    font-weight: 700; font-size: 16px; letter-spacing: 1.6px;
    color: var(--leaf);
  }
</style>
</head>
<body>
<main class="stage">
  <section class="card card-front">
    <div class="accent-tab"></div>
    <div class="brand-name">Coastal Bright Sweep</div>
    <div class="contact-panel">
      <div class="staff-name">JAMIE ELLISON</div>
      <div class="staff-role">CLIENT MANAGER</div>
      <ul class="contact-list">
        <li>
          <svg viewBox="0 0 12 12" aria-hidden="true"><rect x="3" y="0.5" width="6" height="11" rx="1" fill="none" stroke="#fff" stroke-width="1.2"/><circle cx="6" cy="9.6" r="0.7" fill="#fff"/></svg>
          0400 555 182
        </li>
        <li>
          <svg viewBox="0 0 12 12" aria-hidden="true"><rect x="0.5" y="2.5" width="11" height="7.5" fill="#fff"/><path d="M0.8 2.8 L6 6.8 L11.2 2.8" fill="none" stroke="#0f4074" stroke-width="1"/></svg>
          jellison@coastalbrightsweep.com.au
        </li>
        <li>
          <svg viewBox="0 0 12 12" aria-hidden="true"><circle cx="6" cy="6" r="5.5" fill="#fff"/><ellipse cx="6" cy="6" rx="2.3" ry="5.3" fill="none" stroke="#0f4074" stroke-width="0.9"/><line x1="0.7" y1="6" x2="11.3" y2="6" stroke="#0f4074" stroke-width="0.9"/></svg>
          www.coastalbrightsweep.com.au
        </li>
      </ul>
    </div>
  </section>

  <section class="card card-back">
    <div class="back-brand">Bayside Bright Sweep</div>
    <div class="slogan">Turning everyday waste into tomorrow's uses</div>
    <div class="service-line">EVENTS + COMMERCIAL + WASTE</div>
  </section>
</main>
</body>
</html>
```